Charter Tour Boat Webpage Design

We need a web page design for a new business - Kelpwave Trips Orrinbah, We do Fishing Charters, Montague Island Eco Tours, Diving, Whale Watching. We currently have a very basic website up. www.kelpwavetripsorrinbah.com and as you can see we need a much better one.

Thanks!

Mainly fisherman, and families for tours

Business

• page for fishing, montague island eco tours, whale watching.
Contact page, and enquiry page with form.

```html
<!DOCTYPE html>
<html lang="en">
<head>
<meta charset="utf-8">
<title>Kelpwave Trips Orrinbah</title>
<link href="https://fonts.googleapis.com/css2?family=Noto+Serif:wght@400;700&family=Noto+Sans:wght@400;700&family=Roboto+Condensed:wght@400&display=swap" rel="stylesheet">
<style>
:root{
  --header-top:#3545c9;
  --header-bottom:#2733b0;
  --nav:#2c3ab8;
  --footer:#2e45d8;
  --title-yellow:#ffd800;
  --heading:#25507f;
  --text:#444;
  --link:#1e3f7a;
  --rule:#dcdcdc;
  --frame:#6a79c2;
  --orange:#f39200;
  --grey-badge:#c4c4c4;
  --green:#6cc03a;
  --bullet:#3b8ad8;
  --footer-link:#c6cade;
}
*{box-sizing:border-box;margin:0;padding:0}
html,body{width:1021px;height:1200px;overflow:hidden;background:#fff}
body{position:relative;font-family:"Noto Sans",sans-serif;color:var(--text)}
.abs{position:absolute}
.site-header{left:40px;top:6px;width:940px;height:101px;background:linear-gradient(var(--header-top),var(--header-bottom));border-top:2px solid #6b74b8}
.brand{left:0;top:5px;width:330px;text-align:center;font-family:"Noto Serif",serif;font-size:39px;line-height:47px;color:var(--title-yellow)}
.header-art{left:336px;top:0;width:276px;height:99px;background:radial-gradient(ellipse 60px 48px at 50% 50%,rgba(140,195,245,.55),rgba(140,195,245,0) 100%),linear-gradient(90deg,rgba(20,24,70,0) 0%,rgba(20,24,70,.35) 14%,rgba(20,24,70,0) 30%,rgba(20,24,70,0) 70%,rgba(20,24,70,.35) 86%,rgba(20,24,70,0) 100%)}
.account{right:24px;top:6px;font-size:11px;color:#dde;letter-spacing:.3px}
.follow{left:629px;top:61px;font-size:13px;font-weight:700;color:#e8ecff}
.social{top:63px;display:flex;align-items:center;gap:4px;font-size:11px;color:#fff}
.social i{display:inline-block;width:9px;height:9px;border-radius:50%;background:#fff}
.main-nav{left:40px;top:107px;width:940px;height:41px;background:var(--nav);border-top:1px solid #5d6ad0;border-bottom:2px solid #1f2a90}
.menu{position:absolute;top:11px;left:24px;display:flex;font-size:12.5px;font-weight:700;color:#fff;letter-spacing:.3px}
.menu span.sep{margin:0 10px;color:#aab;font-weight:400}
.search{left:641px;top:8px;width:275px;height:24px;background:#fff;font-size:12px;color:#ccd;padding:5px 8px}
.search svg{position:absolute;right:3px;top:2px}
.slider{left:40px;top:169px;width:620px;height:412px;border:1px solid var(--frame);background:linear-gradient(#5aa6e6 0%,#bcdcf5 38%,#2a62c2 50%,#0f3a9a 80%,#1d3f8c 100%)}
.slider svg{position:absolute;top:145px}
h2{font-family:"Roboto Condensed",sans-serif;font-weight:400;font-size:28px;color:var(--heading);letter-spacing:-.3px;line-height:1}
p.copy{font-size:13px;line-height:21px;color:var(--text);letter-spacing:.2px}
.more{display:flex;align-items:center;gap:6px;font-size:13px;font-weight:700;color:var(--link);letter-spacing:.3px}
.rule{height:1px;background:var(--rule)}
.weather{left:684px;top:214px;font-size:11px;color:#2a4a80;display:flex;align-items:center;gap:10px;letter-spacing:.3px}
.badge{font-size:12px;font-weight:700;color:#fff;padding:2px 7px;border-radius:4px}
.deal{left:681px;top:398px;width:217px;height:85px;border:1px solid #ccc;border-radius:6px;background:#fff}
.deal-text{left:7px;top:9px;font-family:"Roboto Condensed",sans-serif;font-size:28px;line-height:35px;color:#666}
.save{left:94px;top:10px;width:40px;height:40px;border-radius:50%;background:#2440b8;color:#fff;font-size:9px;font-weight:700;text-align:center;line-height:11px;padding-top:9px}
.deal-art{left:138px;top:8px;width:68px;height:66px;background:linear-gradient(#f4d36a,#2d8ad1 60%,#41a84a);border-radius:8px}
.photo{border:1px solid var(--frame)}
.reef{left:40px;top:617px;width:300px;height:200px;background:linear-gradient(#2aa6c8,#124a78 45%,#6a5a6a 80%,#2a3050)}
.sunset{left:360px;top:858px;width:300px;height:200px;background:linear-gradient(#f2d1a8,#c7c4c8 35%,#5a74a0 60%,#24426e)}
.video{left:680px;top:617px;width:300px;height:200px;border:1px solid #999;border-radius:4px;background:linear-gradient(#cfcfcf,#9a9a9a)}
.video-screen{left:6px;top:6px;width:287px;height:174px;background:linear-gradient(#5a8cc0,#3a6a98 50%,#1e4a70);overflow:hidden}
.play{left:114px;top:56px;width:58px;height:58px;border-radius:8px;background:rgba(255,255,255,.35)}
.caption{left:0;bottom:0;width:100%;height:54px;background:linear-gradient(rgba(0,0,0,.2),rgba(0,0,0,.6));color:#fff;padding:6px 8px}
.caption b{display:block;font-size:16px;letter-spacing:.5px}
.caption small{font-size:10px}
.controls{left:6px;top:181px;width:287px;height:14px}
.links-col{top:862px;width:140px}
.links-col h3{font-size:16px;font-weight:700;color:#666;letter-spacing:.8px;margin-bottom:5px}
.links-col li{list-style:none;font-size:12.5px;color:#333;line-height:24px;padding-left:28px;position:relative}
.links-col li::before{content:"";position:absolute;left:10px;top:8px;width:8px;height:8px;border-radius:50%;background:radial-gradient(#9cd0ff,var(--bullet))}
.site-footer{left:40px;top:1079px;width:940px;height:81px;background:var(--footer)}
.foot-menu{left:24px;top:15px;display:flex;font-size:12.5px;font-weight:700;color:var(--footer-link);letter-spacing:.3px}
.foot-menu span.sep{margin:0 10px;font-weight:400}
.legal{left:24px;top:47px;font-size:10px;line-height:13px;color:#fff}
.divider{left:653px;top:9px;width:1px;height:60px;background:#c6cade}
.accept{left:686px;top:12px;font-size:12px;font-weight:700;color:var(--title-yellow)}
.cards{left:686px;top:34px;display:flex;gap:7px}
.cards span{width:50px;height:32px;background:#1b2c9c;color:#fff;font-size:8.5px;font-weight:700;display:flex;align-items:center;justify-content:center}
.footer-band{left:40px;top:1160px;width:940px;height:19px;background:var(--footer);border-top:1px solid #8c9ae8}
</style>
</head>
<body>

<header class="site-header abs">
  <div class="brand abs">Kelpwave Trips<br>Orrinbah</div>
  <div class="header-art abs" role="img" aria-label="Two angler silhouettes either side of a compass rose emblem"></div>
  <div class="account abs">You are not logged in &nbsp;|&nbsp; Login or Register</div>
  <div class="follow abs">Follow us</div>
  <div class="social abs" style="left:702px"><i></i>Circlo</div>
  <div class="social abs" style="left:757px"><i></i>Chirpa</div>
  <div class="social abs" style="left:813px"><i></i>Netwo</div>
  <div class="social abs" style="left:866px"><i></i>Feedro</div>
</header>

<nav class="main-nav abs">
  <div class="menu"><span>Home</span><span class="sep">|</span><span>Fishing</span><span class="sep">|</span><span>Montague Island</span><span class="sep">|</span><span>Whale Watching</span><span class="sep">|</span><span>Book Now</span><span class="sep">|</span><span>Contact Us</span></div>
  <div class="search abs">Search our site
    <svg width="20" height="20" viewBox="0 0 20 20"><circle cx="8" cy="8" r="6" fill="none" stroke="#2c3ab8" stroke-width="1.6"/><line x1="12.5" y1="12.5" x2="18" y2="18" stroke="#2c3ab8" stroke-width="1.8"/></svg>
  </div>
</nav>

<div class="slider abs" role="img" aria-label="View from a sailing yacht bow over a deep blue sea under a bright sky">
  <svg style="left:18px" width="74" height="118" viewBox="0 0 74 118"><polyline points="60,10 12,59 60,108" fill="none" stroke="rgba(120,160,230,.75)" stroke-width="16" stroke-linecap="round" stroke-linejoin="round"/></svg>
  <svg style="left:526px" width="74" height="118" viewBox="0 0 74 118"><polyline points="14,10 62,59 14,108" fill="none" stroke="rgba(120,160,230,.75)" stroke-width="16" stroke-linecap="round" stroke-linejoin="round"/></svg>
</div>

<h2 class="abs" style="left:681px;top:167px">Lorem Ipsum Dolor Sit</h2>
<div class="weather abs">
  <span>Weather</span><span style="color:#aaa">|</span><span>Orrinbah</span>
  <svg width="24" height="24" viewBox="0 0 24 24" style="margin-left:-4px"><g stroke="#f5b400" stroke-width="1.6"><line x1="12" y1="1" x2="12" y2="23"/><line x1="1" y1="12" x2="23" y2="12"/><line x1="4" y1="4" x2="20" y2="20"/><line x1="20" y1="4" x2="4" y2="20"/></g><circle cx="12" cy="12" r="6.5" fill="#ffcf1a"/></svg>
  <span style="display:flex;gap:3px;margin-left:-7px"><span class="badge" style="background:var(--orange)">24°C</span><span class="badge" style="background:var(--grey-badge)">11°C</span></span>
</div>
<p class="copy abs" style="left:682px;top:267px;width:292px">Lorem ipsum dolor sit amet, consectetur adipisicing elit, sed do eiusmod tempor incididunt ut labore et dolore magna aliqua. Ut enim ad minim veniam, quis nostrud exercitation ullamco laboris nisi ut aliquip ex</p>
<div class="rule abs" style="left:680px;top:383px;width:300px"></div>

<div class="deal abs">
  <div class="deal-text abs">Deal of<br>the month</div>
  <div class="save abs">SAVE<br>30%</div>
  <div class="deal-art abs" role="img" aria-label="Small sailboat on a wave"></div>
</div>
<p class="copy abs" style="left:680px;top:500px;width:298px">Lorem ipsum dolor sit amet, consectetur adipisicing elit, sed do eiusmod tempor</p>
<a class="more abs" style="left:680px;top:555px">Excepteur sint occaecat cupid
  <svg width="25" height="25" viewBox="0 0 25 25"><circle cx="12.5" cy="12.5" r="12" fill="var(--green)"/><path d="M12.5 5v11M7 11.5l5.5 6 5.5-6" fill="none" stroke="#fff" stroke-width="3"/></svg></a>

<div class="rule abs" style="left:40px;top:596px;width:620px"></div>

<div class="photo reef abs" role="img" aria-label="Colourful coral reef with tropical fish under sun rays"></div>
<h2 class="abs" style="left:360px;top:614px">Lorem Ipsum Dolor Sit</h2>
<p class="copy abs" style="left:360px;top:677px;width:294px">Lorem ipsum dolor sit amet, consectetur adipisicing elit, sed do eiusmod tempor incididunt ut labore et dolore magna aliqua. Ut enim ad minim veniam, quis nostrud exercitation ullamco laboris nisi ut aliquip ex</p>
<a class="more abs" style="left:361px;top:794px">Excepteur sint occaecat cupid
  <svg width="25" height="25" viewBox="0 0 25 25"><circle cx="12.5" cy="12.5" r="12" fill="var(--green)"/><path d="M12.5 5v11M7 11.5l5.5 6 5.5-6" fill="none" stroke="#fff" stroke-width="3"/></svg></a>

<div class="video abs">
  <div class="video-screen abs" role="img" aria-label="Video still of an angler at sea holding a large fish">
    <div class="play abs"><svg width="58" height="58" viewBox="0 0 58 58"><polygon points="22,17 42,29 22,41" fill="rgba(255,255,255,.8)"/></svg></div>
    <div class="caption abs"><b>Lorem ipsum dolor sit</b><small>Ut enim ad minim veniam, quis nostrud exercitation</small></div>
  </div>
  <svg class="controls abs" viewBox="0 0 287 14">
    <rect x="4" y="3" width="2" height="8" fill="#333"/><rect x="8" y="3" width="2" height="8" fill="#333"/>
    <polygon points="24,5 28,5 32,2 32,12 28,9 24,9" fill="#444"/>
    <rect x="62" y="6" width="148" height="2" fill="#666"/><circle cx="114" cy="7" r="4" fill="#555"/>
    <rect x="226" y="4" width="8" height="6" fill="none" stroke="#444"/><rect x="238" y="4" width="8" height="6" fill="none" stroke="#444"/>
    <rect x="251" y="3" width="14" height="8" fill="none" stroke="#444"/>
    <path d="M274 3h-3M274 3v3M281 11h3M284 11v-3" stroke="#444"/>
  </svg>
</div>

<div class="rule abs" style="left:40px;top:837px;width:620px"></div>

<h2 class="abs" style="left:48px;top:855px">Lorem Ipsum Dolor Sit</h2>
<p class="copy abs" style="left:48px;top:918px;width:296px">Lorem ipsum dolor sit amet, consectetur adipisicing elit, sed do eiusmod tempor incididunt ut labore et dolore magna aliqua. Ut enim ad minim veniam, quis nostrud exercitation ullamco laboris nisi ut aliquip ex</p>
<a class="more abs" style="left:49px;top:1035px">Excepteur sint occaecat cupid
  <svg width="25" height="25" viewBox="0 0 25 25"><circle cx="12.5" cy="12.5" r="12" fill="var(--green)"/><path d="M12.5 5v11M7 11.5l5.5 6 5.5-6" fill="none" stroke="#fff" stroke-width="3"/></svg></a>
<div class="photo sunset abs" role="img" aria-label="Orca surfacing in a bay at sunset with seabirds overhead"></div>

<div class="links-col abs" style="left:687px">
  <h3>Lorem ipsum</h3>
  <ul><li>Dolor sit</li><li>Amet</li><li>Consectetur</li><li>Adipisicing</li><li>Elit sed do</li><li>Eiusmod tempor</li><li>Incididunt ut</li></ul>
</div>
<div class="links-col abs" style="left:839px">
  <h3>Lorem ipsum</h3>
  <ul><li>Dolor sit</li><li>Amet</li><li>Consectetur</li><li>Adipisicing</li><li>Elit sed do</li><li>Eiusmod tempor</li><li>Incididunt ut</li></ul>
</div>

<footer class="site-footer abs">
  <div class="foot-menu abs"><span>Home</span><span class="sep">|</span><span>Fishing</span><span class="sep">|</span><span>Montague Island</span><span class="sep">|</span><span>Whale Watching</span><span class="sep">|</span><span>Book Now</span><span class="sep">|</span><span>Contact Us</span></div>
  <div class="legal abs">Copyright © 2012 Kelpwave Trips Orrinbah. All rights reserved<br>Kelpwave Trips Orrinbah • 48 Jetty Parade • Harbourton, NSW 2599 • Phone Number 02 5550 1187</div>
  <div class="divider abs"></div>
  <div class="accept abs">WE ACCEPT</div>
  <div class="cards abs"><span>Coralpay</span><span>Tidecard</span><span>Gullpay</span><span>Harbourex</span></div>
</footer>
<div class="footer-band abs"></div>

</body>
</html>
```